Business Card design for a company called Tallow Flame NI

I need a business card design for my oil fired boiler servicing company. I have a logo design already and Im just looking that incorporated into the business card design. card details; Tallow Flame NI
Oil Burner Servicing - Mid Ulster Area
Service Engineer - Owen Marsh
Mobile 07751364927
email - Tallow.Flame.NI@hearthmail.example
www.tallowflameni.example
I carry out Servicing, Commissioning, Fault Finding, Warranty Validation
Target Market(s)
home owners with oil fired central heating
Industry/Entity Type
Business
Contact Information for Business Card
Tallow Flame NI
Tell. 07751364927
Web: www.tallowflameni.example
email Tallow.Flame.NI@Hearthmail.Example
Servicing Fault Finding Commissioning Warranty Validation
Look and feel

```html
<!DOCTYPE html>
<html lang="en">
<head>
<meta charset="utf-8">
<title>Tallow Flame NI – Business Card</title>
<link href="https://fonts.googleapis.com/css2?family=Arimo:wght@400;700&display=swap" rel="stylesheet">
<style>
  :root {
    --green: #5cb531;
    --green-light: #9bd23c;
    --green-soft: #c9e8a2;
    --text-grey: #4d4d4d;
    --rule-grey: #b5b5b5;
    --card-white: #ffffff;
    --card-shade: #ececec;
    --backdrop: #e4e4e2;
  }
  * { box-sizing: border-box; margin: 0; padding: 0; }
  html, body {
    width: 1200px; height: 950px; overflow: hidden;
    background: var(--backdrop);
    font-family: "Arimo", Arial, sans-serif;
  }
  .canvas {
    width: 1200px; height: 950px;
    display: flex; flex-direction: column;
    align-items: center; justify-content: center; gap: 28px;
  }
  .card {
    width: 760px; height: 434px;
    background: linear-gradient(135deg, var(--card-white) 55%, var(--card-shade));
    box-shadow: 0 6px 18px rgba(0,0,0,0.18);
    position: relative;
  }

  /* back of card */
  .card-back {
    display: flex; flex-direction: column; justify-content: center;
    padding-left: 110px;
  }
  .brand-lockup { display: flex; align-items: center; gap: 16px; }
  .brand-dot {
    width: 58px; height: 58px; border-radius: 50%;
    background: var(--green);
  }
  .brand-name {
    font-size: 44px; font-weight: 700; color: var(--green);
    line-height: 1;
  }
  .brand-tagline {
    margin: 8px 0 0 74px;
    font-size: 11.5px; font-weight: 700; letter-spacing: 1.6px;
    color: var(--green); text-transform: uppercase;
  }
  .services {
    margin-top: 46px;
    font-size: 19px; color: var(--text-grey);
  }
  .services-rule-row {
    margin-top: 18px; display: flex; align-items: center; gap: 10px;
  }
  .social-dot {
    width: 26px; height: 26px; border-radius: 50%;
    background: var(--rule-grey);
  }
  .services-rule {
    flex: 0 0 360px; height: 2px;
    background: linear-gradient(90deg, var(--green), rgba(92,181,49,0));
    margin-left: 8px;
  }

  /* front of card */
  .card-front { display: flex; }
  .emblem-area {
    width: 360px; display: flex; flex-direction: column;
    align-items: center; justify-content: center; gap: 18px;
  }
  .emblem-circle {
    width: 250px; height: 250px; border-radius: 50%;
    background: radial-gradient(circle at 60% 40%, var(--green-light), var(--green));
  }
  .emblem-name {
    font-size: 22px; font-weight: 700; color: var(--green);
  }
  .contact-block {
    flex: 1; padding: 110px 40px 0 0;
    display: flex; flex-direction: column; align-items: flex-end;
  }
  .person-name {
    font-size: 26px; font-weight: 700; color: var(--green);
  }
  .person-role {
    font-size: 20px; color: var(--text-grey); margin-bottom: 10px;
  }
  .contact-line {
    display: flex; align-items: center; gap: 10px;
    font-size: 19px; color: var(--text-grey); line-height: 1.35;
  }
  .contact-line svg { width: 18px; height: 18px; fill: var(--green); }
  .front-brand {
    margin-top: 14px;
    font-size: 38px; font-weight: 700; color: var(--green); line-height: 1;
  }
  .front-tagline {
    margin-top: 5px;
    font-size: 9.5px; font-weight: 700; letter-spacing: 1.4px;
    color: var(--green); text-transform: uppercase;
  }
</style>
</head>
<body>
<main class="canvas">

  <section class="card card-back" aria-label="Card back">
    <div class="brand-lockup">
      <span class="brand-dot"></span>
      <span class="brand-name">Tallow Flame NI</span>
    </div>
    <p class="brand-tagline">Oil Burner Servicing - Mid Ulster Area</p>
    <p class="services">Servicing | Commissioning | Fault Finding | Warranty Validation</p>
    <div class="services-rule-row">
      <span class="social-dot"></span>
      <span class="social-dot"></span>
      <span class="services-rule"></span>
    </div>
  </section>

  <section class="card card-front" aria-label="Card front">
    <div class="emblem-area">
      <div class="emblem-circle"></div>
      <span class="emblem-name">Tallow Flame NI</span>
    </div>
    <div class="contact-block">
      <p class="person-name">Owen Marsh</p>
      <p class="person-role">Service Engineer</p>
      <p class="contact-line">07751364927
        <svg viewBox="0 0 18 18" aria-hidden="true"><path d="M5 1h8a1 1 0 0 1 1 1v14a1 1 0 0 1-1 1H5a1 1 0 0 1-1-1V2a1 1 0 0 1 1-1zm1 2v10h6V3zm3 11a1 1 0 1 0 0 2 1 1 0 0 0 0-2z"/></svg>
      </p>
      <p class="contact-line">07751364927
        <svg viewBox="0 0 18 18" aria-hidden="true"><path d="M1 6c0-2 3-3 8-3s8 1 8 3v1h-4V5.5C12 5 10.5 5 9 5s-3 0-4 .5V7H1zm3 3h10l2 7H2zm5 1.5a2 2 0 1 0 0 4 2 2 0 0 0 0-4z"/></svg>
      </p>
      <p class="contact-line">Tallow.Flame.NI@hearthmail.example
        <svg viewBox="0 0 18 18" aria-hidden="true"><path d="M1 4h16v11H1zm1.5 1.2L9 10l6.5-4.8V5h-13z"/></svg>
      </p>
      <p class="contact-line">www.tallowflameni.example
        <svg viewBox="0 0 18 18" aria-hidden="true"><path d="M9 1a8 8 0 1 1 0 16A8 8 0 0 1 9 1zm0 2v6h5V8h-4V3z"/></svg>
      </p>
      <p class="front-brand">Tallow Flame NI</p>
      <p class="front-tagline">Oil Burner Servicing - Mid Ulster Area</p>
    </div>
  </section>

</main>
</body>
</html>
```